A brochure website design
Product: Nuvel coconut yogurt
Specialty of the product:
Nuvel coconut yogurt is a non dairy yogurt using coconut cream powder and coconut water as its major ingredients. It contains live cultures and is a great alternatives to dairy yogurt.
It is gluten free, soy free, preservative free, lactose free, non-GMO and no artificial sweetener. It is a great choice for paleo diet.
4. About Nuvel
Nuvel is developed by a group of coconut lovers who believe that promoting vegan based diet can contribute to the wellness of the world and the sustainability of living. Our vision is to end cruelty to animal and minimise the world’s reliance on milk farming. We believe that cow milk is belonged to cow BB and God has already provided coconut to us which is actually more suitable to human’s body than dairy product.
5. Our products
Nuvel coconut yogurt 120g
Nuvel coconut yogurt with raspberry 150g
6. Nuvel recipes
7. About coconut
8. Contact us
9. Stores finder
Target Market(s)
Age 18 to 50 . People looking for life style and healthy diet.
Industry/Entity Type
Product
Number of Pages Required
5+ page
Look and feel
Each slider illustrates characteristics of the customer's brand and the style your logo design should communicate.

```html
<!DOCTYPE html>
<html lang="en">
<head>
<meta charset="utf-8">
<title>Nuvel Coconut Yogurt</title>
<link rel="stylesheet" href="https://fonts.googleapis.com/css2?family=Source+Sans+3:wght@300;400;600&display=swap">
<style>
  :root {
    --navy: #062a66;
    --nav-active: #8cc8e8;
    --white: #ffffff;
    --green: #0e9c3c;
    --teal: #1aa0b5;
    --cyan-bar: #12b7e2;
    --ink: #1f2a33;
    --body-text: #4a4a4a;
    --rule: #cfcfcf;
    --ring: #7a4a2a;
    --badge-text: #167f91;
  }
  * { box-sizing: border-box; margin: 0; padding: 0; }
  html, body { width: 1200px; height: 1000px; overflow: hidden; background: var(--white); }
  body { font-family: "Source Sans 3", "Source Sans Pro", sans-serif; position: relative; }

  .site-header { position: absolute; left: 0; top: 0; width: 1200px; height: 85px; background: var(--navy); z-index: 3; }
  .brand { position: absolute; left: 94px; top: 0; width: 172px; height: 99px; background: var(--white);
           border-bottom: 5px solid var(--cyan-bar); display: flex; align-items: center; justify-content: center; }
  .brand-name { font-size: 40px; font-weight: 600; color: var(--green); letter-spacing: 1px; }
  .main-nav { position: absolute; top: 31px; left: 386px; display: flex; gap: 0; }
  .main-nav a { color: var(--white); text-decoration: none; font-size: 16px; margin-right: 32px; white-space: nowrap; }
  .main-nav a.is-active { color: var(--nav-active); }

  .hero { position: absolute; left: 0; top: 85px; width: 1200px; height: 416px; }
  .hero-scene { position: absolute; inset: 0;
    background: linear-gradient(180deg, #5b9fd6 0%, #9fcbec 55%, #bfe4f0 78%, #4fc3d8 86%, #9fdde8 100%); }
  .hero-product { position: absolute; left: 585px; top: 100px; width: 280px; height: 270px; border-radius: 18px 18px 60px 60px;
    background: linear-gradient(180deg, #f2f5f4 0%, #2bb0b5 40%, #25a7ae 70%, #e9ecea 100%); }
  .hero-copy { position: absolute; left: 94px; top: 95px; color: var(--ink); font-weight: 300; }
  .hero-copy .claims { font-size: 25px; line-height: 31px; width: 420px; }
  .hero-copy .diet { font-size: 25px; margin-top: 24px; margin-left: -2px; }
  .btn { display: inline-flex; align-items: center; justify-content: center; background: var(--green); color: var(--white);
         font-size: 14px; font-weight: 600; text-decoration: none; border-radius: 3px; }
  .hero-copy .btn { position: absolute; top: 175px; left: 0; width: 148px; height: 40px; margin-top: 96px; top: 175px; }
  .badges { position: absolute; left: 944px; top: 0; }
  .slider-dots { position: absolute; left: 577px; top: 392px; display: flex; gap: 6px; }
  .slider-dots span { width: 14px; height: 14px; border-radius: 50%; background: #137c9a; }
  .slider-dots span.is-current { background: var(--navy); }

  .about-photo { position: absolute; left: 0; top: 501px; width: 470px; height: 499px;
    background: radial-gradient(ellipse at 35% 55%, #e9c3a6 0%, #f1dccb 35%, #f8f1ea 65%, #ffffff 100%); }
  .about { position: absolute; left: 539px; top: 585px; width: 580px; }
  .about-title { font-size: 25px; font-weight: 600; color: #111; margin-left: 10px; }
  .about-title .accent { color: var(--teal); }
  .title-rule { margin: 6px 0 0 12px; }
  .about p { font-size: 15px; font-weight: 300; line-height: 31px; color: var(--body-text); margin-top: 18px; }
  .about p + p { margin-top: 20px; }
  .about .btn { margin: 26px 0 0 4px; width: 142px; height: 41px; font-weight: 400; font-size: 15px; }
</style>
</head>
<body>
  <header class="site-header">
    <div class="brand"><span class="brand-name">NUVEL</span></div>
    <nav class="main-nav">
      <a class="is-active" href="#">Home</a>
      <a href="#">About&nbsp; Nuvel</a>
      <a href="#">Our products</a>
      <a href="#">Nuvel recipes</a>
      <a href="#">About coconut</a>
      <a href="#">Contact us</a>
      <a href="#">Stores finder</a>
    </nav>
  </header>

  <section class="hero">
    <div class="hero-scene" role="img" aria-label="Tropical beach with blue sky, sea and palm trees"></div>
    <div class="hero-product" role="img" aria-label="Cup of Nuvel coconut yogurt with palm leaf and split coconut"></div>
    <div class="hero-copy">
      <p class="claims">Gluten free, Soy free, Preservative free, Lactose free, non-GMO &amp; no Artificial Sweetener.</p>
      <p class="diet">Great choice for paleo diet.</p>
      <a class="btn" href="#">READ MORE</a>
    </div>
    <svg class="badges" width="140" height="320" viewBox="0 0 140 320">
      <line x1="64" y1="0" x2="64" y2="300" stroke="var(--ring)" stroke-width="5"/>
      <circle cx="64" cy="87" r="62" fill="var(--ring)"/>
      <circle cx="64" cy="87" r="52" fill="var(--white)"/>
      <text x="64" y="86" text-anchor="middle" font-size="23" font-weight="600" fill="var(--badge-text)" font-family="Source Sans 3, sans-serif">DAIRY</text>
      <text x="64" y="110" text-anchor="middle" font-size="23" font-weight="600" fill="var(--badge-text)" font-family="Source Sans 3, sans-serif">FREE</text>
      <circle cx="64" cy="252" r="62" fill="var(--ring)"/>
      <circle cx="64" cy="252" r="52" fill="var(--white)"/>
      <text x="64" y="251" text-anchor="middle" font-size="23" font-weight="600" fill="var(--badge-text)" font-family="Source Sans 3, sans-serif">RICH IN</text>
      <text x="64" y="275" text-anchor="middle" font-size="23" font-weight="600" fill="var(--badge-text)" font-family="Source Sans 3, sans-serif">MCT</text>
    </svg>
    <div class="slider-dots"><span class="is-current"></span><span></span><span></span><span></span></div>
  </section>

  <div class="about-photo" role="img" aria-label="Smiling young woman eating coconut yogurt from a cup"></div>

  <section class="about">
    <h2 class="about-title">About <span class="accent">NUVEL</span></h2>
    <svg class="title-rule" width="128" height="10" viewBox="0 0 128 10">
      <line x1="0" y1="1" x2="128" y2="1" stroke="var(--rule)" stroke-width="2"/>
      <polygon points="57,1 71,1 64,8" fill="var(--green)"/>
    </svg>
    <p>Nuvel coconut yogurt is a non dairy yogurt using coconut cream powder and coconut water as its major ingredients. It contains live cultures and is a great alternatives to dairy yogurt.</p>
    <p>&nbsp;About Nuvel is developed by a group of coconut lovers who believe that promoting vegan based diet can contribute to the wellness of the world and the sustainability of living. Our vision is to end cruelty to animal and minimise the world’s reliance on milk farming. We believe that cow milk is belonged to cow BB and God has already provided coconut to us which is actually more suitable to human’s body than dairy product.</p>
    <a class="btn" href="#">Know More</a>
  </section>
</body>
</html>
```